HAIR EXTENSIONS

We need a web design for a company base in Chicago called Extensions by Corvella. We sale 100% human hair in Brazilian body wave deep wave straight or natural curl, Peruvian body wave straight or deep wave. Malaysian loose straight or body wave, in the chicago land.
We also ship hair to any city or country. We like to see design that use the colors pinks & grays, or would just like to see some design creative with colors thats inviting.

Also I'm using the quillmoss template, Home- banner contact us, about us, Features- product side/left sidebar, Shop- wish list /shopping cart/ tracking your order / checkout/ order received.
Porfolio-filterable 4column portfolio
Blog. Buy now

Industry/Entity Type

Hair

Number of Pages Required

4 page

Colors
aaaaaa
606060
dddddd
eea4c8
d3a5cc
b868aa
a6459a
ffc213
1b1b1b

Requirements
Must have
• I NEED THE DESIGNER TO DO THE 4 PAGE LIKE THIS.
• 1.HOME-PAGE BANNER CONTACT US SOME PRODUCT WITH SIDING IMAGES OF THE TOP PROUDCT
• 2.PRODUCT WITH SHOPPING CART- I WANT SIDING BARS FOR PRODUCT & SHOPPING CART WITH TRACKING YOUR ORDERS CHECK OUT & ORDER RECEIVED.
• 3.PORFOLIO PHOTO-I WANT A FEATURES FOR CUSTOMERS TO UPLOAN THERE PICTURE & BLOG ON THE PAGE
• 4.ABOUT US- TALK ABOUT ARE COMPAMY.
Nice to have
• hello designer
• I was working with a web developer for my site be for i came to pixelharborr & they build a site for me that i liked, You all can view it at www.Extensionsbycorvella.info
• long story short never could get them to finish the project after they got paid!!
• I know, why paid before its finish bad decision. So know I'm here starting over with you all.
• here is a list of my competition site
• www.lockshaventress.com
• www.velmatrade.com
• www.orlitasparlor.com
• So just to give some insight, I'm looking for something like the one i had builded.

```html
<!DOCTYPE html>
<html lang="en">
<head>
<meta charset="utf-8">
<title>BYCORVELLA — Human Hair Extensions</title>
<link rel="stylesheet" href="https://fonts.googleapis.com/css2?family=Open+Sans:ital,wght@0,300;0,400;0,600;0,700;1,400&family=Playfair+Display:wght@400;700&family=Caveat&display=swap">
<style>
:root{
  --ink:#1b1b1b;
  --text:#606060;
  --muted:#aaaaaa;
  --line:#dddddd;
  --page:#f2f2f2;
  --white:#ffffff;
  --accent:#c4122f;
  --dark:#3a3a3a;
  --pink:#eea4c8;
  --mauve:#d3a5cc;
  --orchid:#b868aa;
  --plum:#a6459a;
}
*{box-sizing:border-box;margin:0;padding:0}
html,body{width:1200px;height:2560px;overflow:hidden}
body{font-family:"Open Sans",Arial,sans-serif;color:var(--text);background:var(--page);position:relative}
.wrap{width:1016px;margin:0 auto;position:relative}

.site-header{height:133px;border-top:5px solid var(--ink);display:flex;align-items:center;justify-content:center}
.logo{font-size:36px;font-weight:400;color:var(--ink);letter-spacing:1px}

.main-nav{height:72px;background:var(--white);border-top:1px solid var(--line);border-bottom:1px solid var(--line)}
.main-nav .wrap{display:flex;height:100%;align-items:center}
.nav-links{display:flex;list-style:none;gap:0}
.nav-links li{font-size:12.5px;text-transform:uppercase;color:#555;margin-right:50px}
.nav-links li.active{color:var(--ink)}
.nav-tools{margin-left:auto;display:flex;height:100%}
.cart{display:flex;align-items:center;gap:14px;padding:0 18px;border-left:1px solid var(--line);font-size:11px;line-height:16px;color:var(--muted);text-transform:uppercase}
.cart b{color:var(--ink);font-weight:400;display:block}
.search{width:56px;border-left:1px solid var(--line);border-right:1px solid var(--line);display:flex;align-items:center;justify-content:center}

.hero{margin-top:61px;height:451px;position:relative;overflow:hidden;background:linear-gradient(90deg,#f4f4f4 0%,#d6d6d6 35%,#7a7a7a 55%,#3e3e3e 80%,#333 100%)}
.hero-photo{position:absolute;left:80px;top:0;width:420px;height:451px;background:radial-gradient(ellipse at 50% 45%,#6b4a40 0%,#2d2320 45%,rgba(60,60,70,0) 75%)}
.hero-copy{position:absolute;left:483px;top:140px;font-size:27px;font-weight:300;color:#e8e8e8;line-height:43px;text-transform:uppercase}
.hero-copy strong{font-weight:700;color:var(--white)}
.btn-more{position:absolute;left:492px;top:309px;background:#0d0d0d;color:#fff;font-size:14px;font-weight:600;padding:14px 22px;text-transform:uppercase}
.badge{position:absolute;left:610px;top:292px;width:80px;height:80px;border-radius:50%;background:#fff;border:3px solid #111;text-align:center;font-weight:700;color:#111;font-size:25px;line-height:26px;padding-top:12px}
.badge small{display:block;font-size:15px;font-weight:400}
.arrow{position:absolute;top:201px;width:46px;height:46px;border:3px solid #fff;border-radius:50%;display:flex;align-items:center;justify-content:center}

.promos{display:flex;justify-content:space-between;margin-top:49px}
.promo{width:333px;height:115px;border:1px solid #b9b3a8;background:linear-gradient(90deg,#cfcabf,#ddd8cd 50%,#cbc5ba);display:flex;flex-direction:column;align-items:center;justify-content:center;color:#333}
.promo.alt{background:linear-gradient(90deg,#8f8581,#a59c97 50%,#8b817c);color:#fff;border-color:#7d7470}
.promo-title{font-size:33px;font-weight:700;white-space:nowrap}
.promo-title em{font-family:"Caveat",cursive;font-style:normal;font-weight:400;font-size:36px;margin-right:10px}
.promo-sub{font-size:11px;text-transform:uppercase;margin-top:6px;letter-spacing:.3px;opacity:.85}

.content{position:absolute;top:927px;left:0;width:1200px;height:1159px;background:var(--white);border-top:1px solid var(--line)}
.section-head{display:flex;justify-content:space-between;align-items:center;height:40px}
.section-head h2,.col h3{font-weight:300;color:#333;text-transform:uppercase}
.section-head h2{font-size:27px}
.pager{display:flex;gap:6px}
.pager span{width:30px;height:30px;border:2px solid #bbb;border-radius:50%;display:flex;align-items:center;justify-content:center}
.rule{position:relative;height:14px;margin-top:8px}
.rule::before{content:"";position:absolute;left:0;right:0;top:7px;border-top:1px solid var(--line)}
.rule::after{content:"";position:absolute;left:2px;top:2px;width:10px;height:10px;background:var(--accent);transform:rotate(45deg)}

.products{display:flex;justify-content:space-between;margin-top:29px}
.product{width:234px;height:411px;border:1px solid var(--line)}
.product-img{height:261px}
.product-info{text-align:center;padding-top:12px;height:112px}
.cat{font-size:10px;color:var(--muted);text-transform:uppercase}
.name{font-size:14px;color:#444;margin-top:18px}
.price{margin-top:4px;font-size:17px;font-weight:700;color:var(--ink)}
.price s{font-size:14px;font-weight:400;color:var(--muted);margin-right:6px}
.product-actions{display:flex;border-top:1px solid var(--line);height:36px}
.product-actions span{flex:1;display:flex;align-items:center;justify-content:center;gap:7px;font-size:11px;color:var(--muted);text-transform:uppercase}
.product-actions span+span{border-left:1px solid var(--line)}

.brands{display:flex;justify-content:space-between;margin-top:22px}
.brand{width:130px;height:97px;border:1px solid #ececec;display:flex;align-items:center;justify-content:center;font-size:16px;font-weight:700;color:#111;text-transform:uppercase}

.info{display:flex;justify-content:space-between;margin-top:62px}
.welcome{width:600px}
.testimonial{width:346px}
.info h2{font-size:27px;font-weight:300;color:#333;text-transform:uppercase}
.lead{font-size:17px;color:var(--ink);line-height:24px;margin-top:16px}
.body-copy{font-size:12.5px;line-height:20px;color:#777;margin-top:14px}
.quote{font-size:12.5px;font-style:italic;line-height:21px;color:#666;margin-top:14px}
.author{font-size:16px;font-weight:700;color:var(--ink);margin-top:18px}
.author small{font-size:13px}

.site-footer{position:absolute;top:2086px;left:0;width:1200px;height:381px;background:var(--page);border-top:1px solid var(--line)}
.cols{display:flex;padding-top:52px}
.col h3{font-size:20px}
.col .rule{margin-top:6px}
.col-products{width:377px}
.col-products .rule,.col-contact .rule{width:300px}
.col-contact{width:255px}
.col-contact .rule{width:250px}
.mini{display:flex;gap:19px;margin-top:24px}
.mini-img{width:94px;height:84px;flex:none}
.mini-text{font-size:14px;color:#555;line-height:21px;padding-top:6px}
.stars{color:var(--accent);font-size:10px;letter-spacing:1px}
.mini-price{color:var(--accent);font-size:12px;font-weight:600}
.contact-list{font-size:14px;line-height:23px;color:#666;margin-top:18px}
.payments{display:flex;gap:4px;margin-top:14px}
.payments span{width:35px;height:21px;border:1px solid #ccc;background:#fff;border-radius:2px}
.payments span:nth-child(2n){background:#e9e9e9}

.bottom-bar{position:absolute;top:2467px;left:0;width:1200px;height:93px;background:var(--dark)}
.bottom-bar .wrap{display:flex;align-items:center;height:100%}
.social{display:flex;gap:6px}
.social span{width:40px;height:40px;border-radius:50%}
.copyright{margin-left:auto;font-size:11px;color:#ccc}
.version{margin-left:38px;font-size:13px;color:#ccc}
</style>
</head>
<body>

<header class="site-header"><div class="logo">BYCORVELLA</div></header>

<nav class="main-nav">
  <div class="wrap">
    <ul class="nav-links">
      <li class="active">Home</li><li>About Us</li><li>Shop</li><li>Gallery</li><li>Blog</li><li>Our Services</li><li>Contact Us</li>
    </ul>
    <div class="nav-tools">
      <div class="cart">
        <svg width="16" height="14" viewBox="0 0 16 14"><path d="M1 1h3l2 8h8l1.5-6H5" fill="none" stroke="#333" stroke-width="1.4"/><circle cx="7" cy="12" r="1.3" fill="#333"/><circle cx="13" cy="12" r="1.3" fill="#333"/></svg>
        <div>Shopping Cart<b>(0.00 items)</b></div>
      </div>
      <div class="search"><svg width="14" height="14" viewBox="0 0 14 14"><circle cx="8.5" cy="5.5" r="4" fill="none" stroke="#111" stroke-width="1.8"/><path d="M5.5 8.5L1.5 12.5" stroke="#111" stroke-width="2"/></svg></div>
    </div>
  </div>
</nav>

<div class="wrap">
  <section class="hero">
    <div class="hero-photo" role="img" aria-label="Smiling woman with long dark curly hair extensions"></div>
    <div class="hero-copy">We sell <strong>100%</strong> human hair in<br>Brazilian body wave deep wave<br>straight or <strong>natural curl.</strong></div>
    <div class="btn-more">Read More</div>
    <div class="badge">100<small>%</small></div>
    <div class="arrow" style="left:19px"><svg width="14" height="18" viewBox="0 0 14 18"><path d="M10 2L3 9l7 7" fill="none" stroke="#fff" stroke-width="3"/></svg></div>
    <div class="arrow" style="right:19px"><svg width="14" height="18" viewBox="0 0 14 18"><path d="M4 2l7 7-7 7" fill="none" stroke="#fff" stroke-width="3"/></svg></div>
  </section>

  <div class="promos">
    <div class="promo"><div class="promo-title"><em>Buy</em>Human Hairs</div></div>
    <div class="promo alt"><div class="promo-title"><em>Join Our</em>Newsletter</div><div class="promo-sub">Special offers &nbsp;·&nbsp; Events &nbsp;·&nbsp; Promotions</div></div>
    <div class="promo"><div class="promo-title"><em>Free</em>Shipping $90</div><div class="promo-sub">Free over $125 for international orders</div></div>
  </div>
</div>

<main class="content">
  <div class="wrap" style="padding-top:30px">
    <div class="section-head"><h2>Best Sellers</h2>
      <div class="pager"><span><svg width="8" height="12"><path d="M6 1L1 6l5 5" fill="none" stroke="#999" stroke-width="2"/></svg></span><span><svg width="8" height="12"><path d="M2 1l5 5-5 5" fill="none" stroke="#999" stroke-width="2"/></svg></span></div>
    </div>
    <div class="rule"></div>

    <div class="products">
      <article class="product"><div class="product-img" role="img" aria-label="Customer wearing straight bob hair extensions" style="background:linear-gradient(160deg,#c9d0dc,#5f7fb8 60%,#3d4f75)"></div>
        <div class="product-info"><div class="cat">Sed ut perspiciatis unde</div><div class="name">Sed ut perspiciatised unde</div><div class="price"><s>$ 234.0</s>$180.0</div></div>
        <div class="product-actions"><span><svg width="13" height="12"><path d="M6.5 11L1.5 6a3 3 0 015-3.5A3 3 0 0111.5 6z" fill="none" stroke="#999" stroke-width="1.3"/></svg>Wishlist</span><span><svg width="12" height="12"><path d="M1 3h6M1 3v8h8V6M6 8l5-5" fill="none" stroke="#999" stroke-width="1.3"/></svg>Compare</span></div></article>
      <article class="product"><div class="product-img" role="img" aria-label="Young girl in a pink tutu with styled hair" style="background:linear-gradient(180deg,#d8c3a8,#c9a27c 50%,#e59bb3)"></div>
        <div class="product-info"><div class="cat">Sed ut perspiciatis unde</div><div class="name">Sed ut perspiciatised unde</div><div class="price"><s>$ 234.0</s>$180.0</div></div>
        <div class="product-actions"><span><svg width="13" height="12"><path d="M6.5 11L1.5 6a3 3 0 015-3.5A3 3 0 0111.5 6z" fill="none" stroke="#999" stroke-width="1.3"/></svg>Wishlist</span><span><svg width="12" height="12"><path d="M1 3h6M1 3v8h8V6M6 8l5-5" fill="none" stroke="#999" stroke-width="1.3"/></svg>Compare</span></div></article>
      <article class="product"><div class="product-img" role="img" aria-label="Customer with long braids holding a pink phone" style="background:linear-gradient(160deg,#eadde0,#b08a74 50%,#e2a93c)"></div>
        <div class="product-info"><div class="cat">Sed ut perspiciatis unde</div><div class="name">Sed ut perspiciatised unde</div><div class="price"><s>$ 234.0</s>$180.0</div></div>
        <div class="product-actions"><span><svg width="13" height="12"><path d="M6.5 11L1.5 6a3 3 0 015-3.5A3 3 0 0111.5 6z" fill="none" stroke="#999" stroke-width="1.3"/></svg>Wishlist</span><span><svg width="12" height="12"><path d="M1 3h6M1 3v8h8V6M6 8l5-5" fill="none" stroke="#999" stroke-width="1.3"/></svg>Compare</span></div></article>
      <article class="product"><div class="product-img" role="img" aria-label="Customer with long dark hair in a pink top" style="background:linear-gradient(180deg,#4a3a3a,#8a5c5c 45%,#e85fa8)"></div>
        <div class="product-info"><div class="cat">Sed ut perspiciatis unde</div><div class="name">Sed ut perspiciatised unde</div><div class="price"><s>$ 234.0</s>$180.0</div></div>
        <div class="product-actions"><span><svg width="13" height="12"><path d="M6.5 11L1.5 6a3 3 0 015-3.5A3 3 0 0111.5 6z" fill="none" stroke="#999" stroke-width="1.3"/></svg>Wishlist</span><span><svg width="12" height="12"><path d="M1 3h6M1 3v8h8V6M6 8l5-5" fill="none" stroke="#999" stroke-width="1.3"/></svg>Compare</span></div></article>
    </div>

    <div class="section-head" style="margin-top:72px"><h2>Brands</h2>
      <div class="pager"><span><svg width="8" height="12"><path d="M6 1L1 6l5 5" fill="none" stroke="#999" stroke-width="2"/></svg></span><span><svg width="8" height="12"><path d="M2 1l5 5-5 5" fill="none" stroke="#999" stroke-width="2"/></svg></span></div>
    </div>
    <div class="rule"></div>
    <div class="brands">
      <div class="brand">Alvero Casa</div><div class="brand">Hollis Wade</div><div class="brand">Brenn</div><div class="brand">Marlowe Row</div><div class="brand">Ferro Lane</div><div class="brand">tomas virel</div><div class="brand">Northby</div>
    </div>

    <div class="info">
      <section class="welcome">
        <h2>Welcome to our site!</h2><div class="rule"></div>
        <p class="lead">Sed ut perspiciatis unde omnis iste natus error sit voluptatem accusantium doloremque laudantium, totam rem aperiam.</p>
        <p class="body-copy">Sed ut perspiciatis unde omnis iste natus error sit voluptatem accusantium doloremque laudantium, totam rem aperiam, eaque ipsa quae ab illo inventore veritatis et quasi architecto beatae vitae dicta sunt explicabo. Nemo enim ipsam voluptatem quia voluptas sit aspernatur. Aaut odit aut fugit, sed quia consequuntur magni dolores eos qui ratione voluptatem sequi nesciunt.</p>
      </section>
      <section class="testimonial">
        <h2>Testimonials</h2><div class="rule"></div>
        <p class="quote">“Sed ut perspiciatis unde omnis iste natus error sit voluptatem accusantium doloremque laudantium, totam rem aperiam, eaque ipsa quae ab illo inventore veritatis et quasi architecto beatae vitae dicta sunt explicabo. Nemo enim ipsam voluptatem quia voluptas sit aspernatur”.</p>
        <p class="author">Dara Whitlow, <small>City Name</small></p>
      </section>
    </div>
  </div>
</main>

<footer class="site-footer">
  <div class="wrap cols">
    <div class="col col-products">
      <h3>Top Rated Products</h3><div class="rule"></div>
      <div class="mini"><div class="mini-img" role="img" aria-label="Customer with styled hair" style="background:linear-gradient(160deg,#5a3b30,#7a9a5a)"></div><div class="mini-text">Sed ut perspiciatis unde hnis<br>iste natus error sit.<div class="stars">★★★★</div><div class="mini-price">$175.00</div></div></div>
      <div class="mini"><div class="mini-img" role="img" aria-label="Hair care products on a table" style="background:linear-gradient(160deg,#b9a58c,#6f7d5a)"></div><div class="mini-text">Sed ut perspiciatis unde hnis<br>iste natus error sit.<div class="stars">★★★</div><div class="mini-price">$175.00</div></div></div>
    </div>
    <div class="col col-products">
      <h3>On Sale</h3><div class="rule"></div>
      <div class="mini"><div class="mini-img" role="img" aria-label="Customer with dark wavy hair" style="background:linear-gradient(160deg,#e0d6d6,#5a3c34)"></div><div class="mini-text">Sed ut perspiciatis unde hnis<br>iste natus error sit.<div class="mini-price" style="margin-top:8px">$175.00</div></div></div>
      <div class="mini"><div class="mini-img" role="img" aria-label="Two customers posing together" style="background:linear-gradient(160deg,#3b2a26,#a98a78)"></div><div class="mini-text">Sed ut perspiciatis unde hnis<br>iste natus error sit.<div class="mini-price" style="margin-top:8px">$175.00</div></div></div>
    </div>
    <div class="col col-contact">
      <h3>Contact Us</h3><div class="rule"></div>
      <div class="contact-list">t: 1-866-555-0142<br>f: 1-866-555-0143<br>e: contact@quillmoss.com</div>
      <h3 style="margin-top:48px">Payment Us</h3><div class="rule"></div>
      <div class="payments"><span></span><span></span><span></span><span></span><span></span><span></span><span></span></div>
    </div>
  </div>
</footer>

<div class="bottom-bar">
  <div class="wrap">
    <div class="social"><span style="background:#3b4f9a"></span><span style="background:#2a9ee0"></span><span style="background:#1c78b4"></span><span style="background:#d9232b"></span></div>
    <div class="copyright">© 2014 -bycorvella.com. all copyrights are reserved</div>
    <div class="version">C4</div>
  </div>
</div>

</body>
</html>
```